Pinecrest Marketing 8 page broshure

I need a design for an 8 page 8.5 X 11 booklet for my company. Our company colors are dark blue, light blue, and white. I am uploading some files for language that you may use. One of the files is our logo. please use the phrase: To us business is a contact sport as well as Pinecrest Marketing is your complete marketing solution. Include something about we offer web and brochure design.as well as social media marketing.

Dear Kalvik at Artisan Forge, Dear Kalvik, we just spoke on the phone about my project for Pinecrest Marketing Group sales brochure. As we discussed there are several things wrong with the final version that the Brame sent to me. First of all the design is completely wrong, It is designed to be 8.5 x 11 when it should be designed to be 8.5 X 5.5 and the fold in the booklet should be the 8.5 side. In other words if you take and 8.5 x 11 piece of paper and fold in half that makes a booklet of 8.5 x 5.5. The other problem that were having with this is that there is no page covering our CRM product which is very important to our service offerings. I have sent you files that cover the CRM but for some reason it wasn't put in. Two small changes, on the front cover I see that we have on the very bottom of the of the page there is a line that says as well as Pinecrest marketing is your complete marketing solution. I would like that line taken out. On the back cover I would like to change the address at the very bottom of the page the new address will be 41753 Calder Rd., Westlake, OH 44192 I think if those changes are made we are about ready to go. Don't misunderstand we love your work, you guys have worked hard and the design is very good there just so's changes to make. Thank you very much, Carl Ibsen

Target Market(s)

Any business that needs help with increasing their sales and marketing in their company. We also have a fully customizable CRM so they may track the leads that are in their pipeline as well as those leads we bring in to their pipeline. On the marketing side we offer many services. Two things that I could not download was we do website design srvices and social media marketing.

Industry/Entity Type

It Company

Font styles to use
Sans Serif

Colors
0555a3
00a990
ffffff

Requirements
Must have
• Company logo on front cover, Stress the various services we offer on the marketing side, stress the CRM - very important. Feel free to use any of the dowloads I am sending to you for text.
Nice to have
• Very professional and elegant presentation.
Should not have
• Should not have any drawings or things that look out of place. Stock picture are fine as long as they have something to do with marketing or CRM.

```html
<!DOCTYPE html>
<html lang="en">
<head>
<meta charset="utf-8">
<title>Pinecrest Marketing Group – Booklet Pages</title>
<link rel="stylesheet" href="https://fonts.googleapis.com/css2?family=Open+Sans:wght@300;400;600&display=swap">
<style>
:root{
  --backdrop:#555555;
  --navy:#0555a3;
  --blue:#1a73c9;
  --sky:#3d9be0;
  --pale:#d4e7f7;
  --ink:#4a4a4a;
  --paper:#ffffff;
  --grey:#cfd1d4;
}
*{margin:0;padding:0;box-sizing:border-box}
html,body{width:1200px;height:1200px;overflow:hidden;background:var(--backdrop)}
body{position:relative;font-family:"Open Sans",Arial,sans-serif}
.page{position:absolute;left:542px;width:88px;height:114px;overflow:hidden;background:var(--paper)}
.page.cover{height:107px}
.sheet{position:absolute;left:0;top:0;width:440px;height:570px;transform:scale(.2);transform-origin:0 0;background:var(--paper)}
.art{position:absolute;left:0;top:0;width:440px;height:570px}
.block{position:absolute}
.title{font-weight:300;color:var(--sky);font-size:34px;letter-spacing:2px}
.heading{font-weight:300;color:var(--sky);font-size:17px;line-height:20px}
.subhead{font-weight:600;color:var(--blue);font-size:9px;line-height:12px;margin-bottom:2px}
.para{font-size:8px;line-height:10.5px;color:var(--ink);text-align:justify;margin-bottom:7px}
.para.dark{color:#222}
.list{list-style:none;font-size:8px;line-height:12px;color:var(--blue);margin-bottom:8px}
.list li::before{content:"› ";color:var(--navy)}
.list.plain li{color:var(--ink)}
.brand-name{font-weight:600;color:var(--navy);font-size:14px;text-align:center}
.icon-grid{display:grid;grid-template-columns:repeat(5,1fr);gap:18px 20px}
.icon-grid figure{text-align:center}
.icon-grid span{display:block;width:36px;height:26px;border-radius:8px;background:var(--sky);margin:0 auto 4px}
.icon-grid figcaption{font-size:7px;color:var(--ink)}
.side-bar{position:absolute;right:0;top:0;width:36px;height:340px;background:var(--navy)}
.side-bar p{position:absolute;left:10px;top:30px;writing-mode:vertical-rl;color:#fff;font-size:11px;font-weight:300;letter-spacing:1px}
</style>
</head>
<body>

<!-- Cover -->
<section class="page cover" style="top:0">
  <div class="sheet">
    <svg class="art" viewBox="0 0 440 570">
      <defs>
        <linearGradient id="cityTone" x1="0" y1="0" x2="0" y2="1">
          <stop offset="0" stop-color="#a9d2f2"/><stop offset=".5" stop-color="#4c9ee0"/><stop offset="1" stop-color="#1d6cba"/>
        </linearGradient>
      </defs>
      <circle cx="220" cy="55" r="24" fill="var(--navy)"/>
      <path role="img" aria-label="City skyline photograph in blue tones" d="M0 150 Q220 230 440 120 L440 390 Q220 500 0 380 Z" fill="url(#cityTone)"/>
      <path d="M0 385 Q220 505 440 400" stroke="var(--navy)" stroke-width="10" fill="none"/>
      <path d="M20 410 Q220 500 420 430" stroke="var(--sky)" stroke-width="3" fill="none"/>
    </svg>
    <p class="block brand-name" style="left:0;top:88px;width:440px">Pinecrest Marketing Group</p>
    <p class="block heading" style="left:0;top:458px;width:440px;text-align:center;font-size:14px">To us, business is a contact sport</p>
    <p class="block para dark" style="left:0;top:484px;width:440px;text-align:center;font-weight:600">Pinecrest Marketing Group is your complete marketing solution</p>
  </div>
</section>

<!-- About us -->
<section class="page" style="top:118px">
  <div class="sheet">
    <svg class="art" viewBox="0 0 440 570">
      <defs>
        <linearGradient id="greyFade" x1="0" y1="0" x2="0" y2="1">
          <stop offset="0" stop-color="#fff"/><stop offset="1" stop-color="#c3c5c9"/>
        </linearGradient>
      </defs>
      <circle role="img" aria-label="Globe graphic" cx="385" cy="75" r="40" fill="var(--navy)"/>
      <path d="M0 105 Q220 160 440 120" stroke="var(--navy)" stroke-width="7" fill="none"/>
      <path d="M0 118 Q220 168 440 135" stroke="var(--sky)" stroke-width="2" fill="none"/>
      <rect x="0" y="400" width="440" height="170" fill="url(#greyFade)"/>
      <path d="M0 410 Q220 370 440 405" stroke="var(--navy)" stroke-width="7" fill="none"/>
      <path d="M0 420 Q220 380 440 418" stroke="var(--sky)" stroke-width="2" fill="none"/>
    </svg>
    <h1 class="block title" style="left:38px;top:25px">ABOUT US</h1>
    <div class="block" style="left:30px;top:142px;width:380px">
      <h2 class="heading" style="margin-bottom:8px">Who is Pinecrest Marketing Group?</h2>
      <p class="para">Pinecrest Marketing Group helps growing companies build steady sales through lead generation, appointment setting, direct mail, email campaigns, web design, brochure design and social media marketing. We work with firms of every size, from local service providers to national manufacturers, and we shape every program around the buyers they want to reach. Our callers, writers and designers share one goal: to put qualified prospects in front of your sales team and help them close more business each month.</p>
      <p class="para">Our team works as an extension of your own sales staff. We learn your products, your market and your message, then we carry that message to decision makers by phone, by mail and online. Each lead is checked, scored and delivered with full notes so your people know exactly who they are calling and why.</p>
      <p class="para">Every program is backed by a fully customizable CRM that tracks the leads already in your pipeline as well as the leads we bring in. You see the results in real time, with clear reports that show cost, progress and return on every campaign we run together.</p>
    </div>
    <div class="block" style="left:30px;top:438px;width:380px">
      <h2 class="heading" style="margin-bottom:8px">Our Mission Statement</h2>
      <p class="para">We deliver measurable growth with honest reporting, proven methods and a partner who treats your goals as our own. To us, business is a contact sport, and we work every day to earn the trust of the clients we serve and the prospects we reach on their behalf. Our success is measured only by yours.</p>
    </div>
  </div>
</section>

<!-- Why partner -->
<section class="page" style="top:243px">
  <div class="sheet">
    <svg class="art" viewBox="0 0 440 570">
      <defs>
        <linearGradient id="glassTone" x1="0" y1="0" x2="1" y2="1">
          <stop offset="0" stop-color="#eef3f8"/><stop offset="1" stop-color="#7ea8cf"/>
        </linearGradient>
        <linearGradient id="archTone" x1="0" y1="0" x2="1" y2="1">
          <stop offset="0" stop-color="#b9cde0"/><stop offset=".5" stop-color="#2d5f92"/><stop offset="1" stop-color="#16375a"/>
        </linearGradient>
      </defs>
      <rect role="img" aria-label="Glass office building photograph" x="0" y="0" width="440" height="570" fill="url(#glassTone)"/>
      <rect x="50" y="0" width="330" height="440" fill="#ededef"/>
      <path role="img" aria-label="Curved glass architecture photograph" d="M0 470 Q260 480 440 330 L440 570 L0 570 Z" fill="url(#archTone)"/>
      <path d="M0 470 Q260 480 440 330" stroke="#fff" stroke-width="6" fill="none"/>
    </svg>
    <div class="block" style="left:70px;top:22px;width:295px">
      <h2 class="heading" style="margin-bottom:12px">Why partner with<br>Pinecrest Marketing Group?</h2>
      <p class="para">Every lead we generate is tracked, scored and delivered with the details your team needs to close the sale quickly. We do not hand over a list of names; we hand over real conversations with people who have asked to hear from you.</p>
      <p class="para">From the first call to the signed contract, our CRM keeps every contact, note and follow-up in one place. Your managers can see which campaigns work, which prospects are ready and where each deal stands at any moment of the day.</p>
      <p class="para">Our staff is trained in your industry and speaks to buyers with care and respect. We protect your brand in every call, every letter and every email we send.</p>
      <p class="para">We keep costs clear and fixed, so you always know what each lead costs and what it returns. There are no hidden fees and no long contracts, only steady results.</p>
      <p class="para">To us, business is a contact sport, and we play to win for every client we serve. When you grow, we grow, and that keeps our whole team focused on your success.</p>
    </div>
  </div>
</section>

<!-- Services menu -->
<section class="page" style="top:367px">
  <div class="sheet">
    <svg class="art" viewBox="0 0 440 570">
      <defs>
        <linearGradient id="techTone" x1="0" y1="0" x2="1" y2="1">
          <stop offset="0" stop-color="#0b1d2c"/><stop offset=".55" stop-color="#3a7aa3"/><stop offset="1" stop-color="#13283c"/>
        </linearGradient>
      </defs>
      <rect role="img" aria-label="Photograph of a hand touching a digital business chart" x="0" y="0" width="440" height="222" fill="url(#techTone)"/>
    </svg>
    <div class="block" style="left:30px;top:226px;width:380px">
      <h2 class="heading" style="margin-bottom:6px">Services Menu</h2>
      <p class="para">Choose the services that fit your goals, or combine them into one plan.</p>
      <p class="para">Each program is built around your sales targets and your budget, with clear reports every week.</p>
      <p class="para">Lead generation, appointment setting, direct mail, email campaigns, web design, brochure design and social media marketing, all managed by one team.</p>
      <p class="para">Every lead is loaded into your CRM so nothing slips through the cracks.</p>
      <p class="para">Ask us how a combined program can lower your cost per lead and raise the number of deals your team closes each quarter.</p>
    </div>
    <div class="block icon-grid" role="img" aria-label="Service icons" style="left:30px;top:448px;width:380px">
      <figure><span></span><figcaption>Leads</figcaption></figure>
      <figure><span></span><figcaption>Mail</figcaption></figure>
      <figure><span></span><figcaption>Email</figcaption></figure>
      <figure><span></span><figcaption>Web</figcaption></figure>
      <figure><span></span><figcaption>Social</figcaption></figure>
      <figure><span></span><figcaption>CRM</figcaption></figure>
      <figure><span></span><figcaption>Calls</figcaption></figure>
      <figure><span></span><figcaption>Print</figcaption></figure>
      <figure><span></span><figcaption>Search</figcaption></figure>
      <figure><span></span><figcaption>Reports</figcaption></figure>
    </div>
  </div>
</section>

<!-- Lead generation -->
<section class="page" style="top:491px">
  <div class="sheet">
    <svg class="art" viewBox="0 0 440 570">
      <defs>
        <linearGradient id="deskTone" x1="0" y1="0" x2="1" y2="1">
          <stop offset="0" stop-color="#eef5fc"/><stop offset=".6" stop-color="#8fc1ea"/><stop offset="1" stop-color="#2f83cf"/>
        </linearGradient>
      </defs>
      <rect role="img" aria-label="Small business chart graphic" x="370" y="25" width="45" height="38" rx="6" fill="var(--sky)"/>
      <path role="img" aria-label="Photograph of a pen and reports on a desk" d="M0 375 Q220 350 440 370 L440 570 L0 570 Z" fill="url(#deskTone)"/>
    </svg>
    <div class="block" style="left:50px;top:56px;width:360px">
      <h2 class="heading" style="margin-bottom:10px;font-size:15px">Business to Business Lead Generation</h2>
      <p class="para">Our callers reach decision makers in your target market and qualify each prospect before the lead reaches you. We confirm budget, timing and need, so your sales staff spends time only with buyers who are ready to talk and able to act.</p>
      <p class="para">Leads are loaded into your CRM with full notes, so you can follow progress from first contact to closed deal. Managers see every call, every result and every follow-up date in one simple view.</p>
      <p class="para">We build calling lists from trusted sources and clean them before any campaign begins. This keeps your cost per lead low and your reach high across the markets you serve.</p>
      <p class="para">Programs can run for a single month or all year, and they can grow as your team grows. You stay in control of the volume and the targets at every stage.</p>
      <p class="para" style="color:var(--sky)">Learn more about our lead programs today.</p>
    </div>
  </div>
</section>

<!-- Direct mail and email -->
<section class="page" style="top:616px">
  <div class="sheet">
    <svg class="art" viewBox="0 0 440 570">
      <path d="M0 8 Q220 60 440 5 L440 0 L0 0 Z" fill="var(--navy)"/>
      <path d="M0 20 Q220 65 440 18" stroke="var(--sky)" stroke-width="2" fill="none"/>
      <rect role="img" aria-label="Mail graphic" x="355" y="105" width="50" height="36" rx="5" fill="var(--sky)"/>
      <path d="M0 320 Q220 270 440 300" stroke="var(--navy)" stroke-width="8" fill="none"/>
      <path d="M0 332 Q220 285 440 314" stroke="var(--sky)" stroke-width="2" fill="none"/>
      <rect role="img" aria-label="Email graphic" x="235" y="333" width="30" height="22" rx="4" fill="var(--sky)"/>
      <rect role="img" aria-label="Figure carrying a mail envelope graphic" x="355" y="455" width="45" height="75" rx="6" fill="var(--pale)"/>
    </svg>
    <div class="block" style="left:30px;top:34px;width:330px">
      <h2 class="heading" style="margin-bottom:8px">Direct Mailing Services</h2>
      <p class="para">Targeted mailing lists, print design and postage handled from start to finish so your message lands with the right buyers at the right time.</p>
      <ul class="list plain"><li>Custom lists built for your market</li><li>Design and print of every piece</li></ul>
      <p class="para">Each mailing is timed to work with our calling and email programs, so prospects hear from you more than once and remember your name when they are ready to buy. Responses are tracked and added to your CRM.</p>
      <p class="para">We handle sorting, postal rates and delivery reports, leaving your team free to focus on the conversations that follow each drop.</p>
    </div>
    <h2 class="block heading" style="left:272px;top:335px;font-size:14px">Effective Email Campaigns</h2>
    <div class="block" style="left:30px;top:390px;width:300px">
      <p class="subhead">What we provide:</p>
      <ul class="list">
        <li>Custom email templates built for your brand</li><li>List building and list cleanup</li><li>Scheduled and automated sends</li><li>Open and click reports each week</li><li>Follow up sequences for new leads</li>
      </ul>
    </div>
  </div>
</section>

<!-- Cost per lead -->
<section class="page" style="top:741px">
  <div class="sheet">
    <svg class="art" viewBox="0 0 440 570">
      <defs>
        <linearGradient id="greyBand" x1="0" y1="0" x2="0" y2="1">
          <stop offset="0" stop-color="#e4e5e7"/><stop offset="1" stop-color="#c2c4c7"/>
        </linearGradient>
      </defs>
      <rect x="0" y="300" width="440" height="270" fill="url(#greyBand)"/>
      <path d="M0 300 Q220 330 440 265 L440 0 L0 0 Z" fill="var(--paper)"/>
      <path d="M0 300 Q220 330 440 268" stroke="var(--navy)" stroke-width="7" fill="none"/>
      <circle role="img" aria-label="Globe graphic" cx="360" cy="285" r="30" fill="var(--navy)"/>
    </svg>
    <div class="block" style="left:30px;top:24px;width:380px">
      <h2 class="heading" style="margin-bottom:8px">Compare The Cost Per Lead</h2>
      <p class="para">Hiring, training and managing an inside sales team costs far more than a dedicated lead program. Salaries, benefits, desks, phones and turnover add up quickly, and results can take months to appear.</p>
      <p class="para">With Pinecrest, you pay only for the work that moves prospects into your pipeline. Our trained staff starts within days, and every lead comes with notes and a clear next step.</p>
      <p class="para">Most clients find that their cost per qualified lead drops sharply in the first quarter, while the number of closed deals rises.</p>
      <p class="para">Ask us for a side by side cost review based on your own numbers.</p>
    </div>
    <div class="block" style="left:30px;top:330px;width:380px">
      <h2 class="heading" style="margin-bottom:8px">The Executive Sales Search Team</h2>
      <p class="para">We help you find, screen and place proven sales professionals ready to grow your revenue. Our search team knows what strong sales people look like because we work beside them every day.</p>
      <p class="para">Each candidate is interviewed, tested and checked before you meet them. You see only people who match your market, your products and your culture, which saves your managers many hours of work.</p>
      <p class="para">Placements are backed by a follow up period, so you can hire with confidence and keep building the team your business needs.</p>
    </div>
  </div>
</section>

<!-- CRM -->
<section class="page" style="top:866px">
  <div class="sheet">
    <svg class="art" viewBox="0 0 440 570">
      <defs>
        <linearGradient id="towerTone" x1="0" y1="0" x2="0" y2="1">
          <stop offset="0" stop-color="#ffffff"/><stop offset=".4" stop-color="#b8d3ea"/><stop offset="1" stop-color="#1f5f9c"/>
        </linearGradient>
      </defs>
      <rect role="img" aria-label="Photograph of a modern office tower" x="220" y="330" width="220" height="240" fill="url(#towerTone)"/>
    </svg>
    <div class="block" style="left:30px;top:26px;width:380px">
      <h2 class="heading" style="margin-bottom:8px;font-size:15px;line-height:18px">Pinecrest CRM Sales System<br>Track Every Lead In Your Pipeline<br>Pinecrest Marketing Group CRM Service</h2>
      <p class="para">Our fully customizable CRM tracks the leads already in your pipeline as well as the leads we bring in for you. Every contact, call and note is kept in one secure place that your whole team can reach from any desk or device.</p>
      <p class="para">Set up your own stages, fields and reports, and see at a glance which deals are moving and which need attention.</p>
    </div>
    <div class="block" style="left:30px;top:222px;width:200px">
      <p class="subhead">Contact Management</p>
      <ul class="list plain"><li>Full contact history</li><li>Notes and attachments</li></ul>
      <p class="subhead">Pipeline Tracking</p>
      <ul class="list plain"><li>Custom deal stages</li><li>Forecasts by rep</li><li>Lead source reports</li></ul>
      <p class="subhead">Tasks and Reminders</p>
      <ul class="list plain"><li>Follow up alerts</li><li>Shared team calendar</li></ul>
      <p class="para" style="color:var(--sky)">Ask for a free CRM demo today.</p>
    </div>
  </div>
</section>

<!-- Web, social, brochure -->
<section class="page" style="top:990px">
  <div class="sheet">
    <div class="side-bar"><p>Pinecrest Marketing Group</p></div>
    <svg class="art" viewBox="0 0 440 570">
      <circle role="img" aria-label="Globe graphic" cx="440" cy="490" r="42" fill="var(--navy)"/>
    </svg>
    <div class="block" style="left:30px;top:22px;width:350px">
      <p class="para">Pinecrest Marketing Group offers a full set of design and online services to support every campaign. Your brand looks the same on your website, in your brochures and across every social network, so buyers know and trust your name.</p>
      <p class="para">We plan each project with your sales goals in mind and measure the results.</p>
      <p class="subhead">Web Design Services</p>
      <p class="para">A clean, modern site that loads fast, works on every device and turns visitors into qualified leads that flow into your CRM.</p>
      <p class="subhead">Social Media Marketing</p>
      <p class="para">We plan, write, post and measure content across the networks your buyers use every day, building steady interest in your company.</p>
      <p class="subhead">Brochure Design</p>
      <p class="para">Printed pieces that match your brand and support every sales call, from simple flyers to full booklets.</p>
      <p class="subhead">Search Marketing</p>
      <p class="para">Ads and content that help buyers find you first when they search for the services you provide.</p>
      <p class="subhead">Reporting</p>
      <p class="para">Clear monthly reports show traffic, leads and cost, so you always know what your marketing returns.</p>
      <p class="para">Call our team today to plan your complete marketing solution.</p>
    </div>
  </div>
</section>

<!-- Back cover -->
<section class="page" style="top:1114px">
  <div class="sheet">
    <svg class="art" viewBox="0 0 440 570">
      <defs>
        <linearGradient id="backCity" x1="0" y1="0" x2="0" y2="1">
          <stop offset="0" stop-color="#2a7cc8"/><stop offset=".5" stop-color="#7fb8e6"/><stop offset="1" stop-color="#3f8fd4"/>
        </linearGradient>
      </defs>
      <path role="img" aria-label="City skyline photograph in blue tones" d="M0 70 Q220 0 440 60 L440 570 L0 570 Z" fill="url(#backCity)"/>
      <path d="M0 62 Q220 -8 440 52" stroke="var(--navy)" stroke-width="8" fill="none"/>
    </svg>
  </div>
</section>

</body>
</html>
```